Personal training poster - 1200X900mm

Poster to promote my new personal training service at my gym. The poster will be printed and put into an aframe to be seen by people walking past my gym. It needs to be simple and eye catching with the text i have put in the must haves. The text and image should be the prominent parts of the design.

Target Market(s)

30-50 year old females

Industry/Entity Type

Fitness

Font styles to use
Sans Serif

Requirements
Must have
• my logo
• exercise graphic
• Must include the following text:
• Are you looking for a personal trainer? Our expert trainers can help you achieve you take your health and fitness back!
• Contact details:
• 1300452908
• info@brightmotiongym.example.com.au
• Located under the Harbourside Club

```html
<!DOCTYPE html>
<html lang="en">
<head>
<meta charset="utf-8">
<title>Personal Training Poster – Bright Motion Gym</title>
<link rel="stylesheet" href="https://fonts.googleapis.com/css2?family=Exo+2:wght@300;400;800;900&display=swap">
<style>
  :root {
    --poster-yellow: #fdd20a;
    --glow-yellow: #fff6b8;
    --brand-blue: #1f5fae;
    --ink: #1c1c1c;
    --sticker-white: #ffffff;
    --page-bg: #e9e9e9;
  }
  * { margin: 0; padding: 0; box-sizing: border-box; }
  html, body {
    width: 1006px;
    height: 1200px;
    overflow: hidden;
    background: var(--page-bg);
  }
  .poster {
    position: absolute;
    left: 53px;
    top: 0;
    width: 900px;
    height: 1200px;
    background:
      radial-gradient(ellipse 330px 300px at 450px 760px, var(--glow-yellow) 0%, rgba(255,246,184,0) 100%),
      var(--poster-yellow);
    font-family: "Exo 2", sans-serif;
    color: var(--ink);
    text-align: center;
  }
  .headline {
    position: absolute;
    left: 0;
    top: 64px;
    width: 100%;
    font-weight: 900;
    font-size: 110px;
    line-height: 93px;
    letter-spacing: -4px;
    color: var(--brand-blue);
    text-transform: uppercase;
  }
  .headline span { display: block; }
  .sticker {
    position: absolute;
    left: 680px;
    top: 30px;
    width: 152px;
    height: 152px;
  }
  .intro {
    position: absolute;
    left: 0;
    top: 455px;
    width: 100%;
    font-weight: 400;
    font-size: 35px;
    line-height: 46px;
    letter-spacing: 0.5px;
  }
  .brand {
    position: absolute;
    left: 0;
    top: 720px;
    width: 100%;
    display: flex;
    align-items: center;
    justify-content: center;
    gap: 18px;
  }
  .brand-dot {
    width: 34px;
    height: 34px;
    border-radius: 50%;
    background: var(--brand-blue);
  }
  .brand-name {
    font-weight: 800;
    font-size: 58px;
    letter-spacing: 1px;
    color: var(--brand-blue);
    text-transform: uppercase;
  }
  .contact {
    position: absolute;
    left: 0;
    top: 920px;
    width: 100%;
    font-size: 36px;
    line-height: 48px;
    font-weight: 400;
  }
  .contact .phone {
    font-weight: 800;
    font-size: 56px;
    line-height: 74px;
    color: var(--brand-blue);
    letter-spacing: 1px;
  }
</style>
</head>
<body>
  <main class="poster">
    <h1 class="headline">
      <span>Are you</span>
      <span>looking for a</span>
      <span>personal</span>
      <span>trainer?</span>
    </h1>

    <svg class="sticker" viewBox="0 0 152 152" aria-label="Act now sticker">
      <circle cx="76" cy="76" r="72" fill="var(--sticker-white)" stroke="#d8d8d8" stroke-width="2"/>
      <g transform="rotate(18 76 76)" font-family="'Exo 2', sans-serif" font-weight="900" font-size="44" fill="var(--ink)" text-anchor="middle">
        <text x="76" y="70">ACT</text>
        <text x="76" y="112">NOW</text>
      </g>
    </svg>

    <p class="intro">Our expert trainers can help you get<br>your health and fitness back!</p>

    <div class="brand">
      <span class="brand-dot"></span>
      <span class="brand-name">Bright Motion Gym</span>
    </div>

    <section class="contact">
      <p>Contact details:</p>
      <p class="phone">1300 452 908</p>
      <p>info@brightmotiongym.example.com.au</p>
      <p>Located under the Harbourside Club</p>
    </section>
  </main>
</body>
</html>
```